Lunaryth needs a elegant mystical business card design

The theme of Lunaryth is centered on Kemetic/Ancient Egyptian Spirituality. My business sells handmade scented candles, mystic oils, body sprays, tarot readings and more. I would like my business card to reflect an elegant and mystical look. Hieroglyphs around the borders would be a cool idea. Also, the main colors I am working with is Black and Gold= colors of royalty. Black background. The business card will be double sided. The back will have the logo, and the front will have the basic information (ie name, title, business, phone, email, website, etc..)

Target Market(s)

The target market are people into metaphysics, holistic healing, ancient Egyptian culture, aromatherapy, occult science, and the esoteric.

Industry/Entity Type

Business

Contact Information for Business Card

Name: Marisol T. Pike
Title: Owner
Business: LUNARYTH
Phone: 555.210.4473
Website: www.Lunaryth.example
Facebook, Instagram, and twitter icons

Font styles to use
Serif
Decorative

Requirements
Must have
• My logo, and website.
Nice to have
• Ancient Egyptian hieroglyphs, Elegant designs around the border, or encircling the logo.

```html
<!DOCTYPE html>
<html lang="en">
<head>
<meta charset="utf-8">
<title>Lunaryth — Business Card</title>
<link rel="stylesheet" href="https://fonts.googleapis.com/css2?family=Cinzel:wght@400;600;700&display=swap">
<style>
  :root {
    --stage: #e7e1d7;
    --card-black: #070606;
    --gold: #c9a063;
    --gold-soft: #a9844f;
    --bronze-dark: #1c130c;
    --bronze-mid: #5a3f26;
    --bronze-light: #7a5834;
  }
  * { box-sizing: border-box; margin: 0; padding: 0; }
  html, body { width: 1200px; height: 1200px; overflow: hidden; }
  body {
    background: var(--stage);
    font-family: "Cinzel", "Times New Roman", serif;
    position: relative;
  }
  .card {
    position: absolute;
    left: 237px;
    width: 723px;
    height: 434px;
    border-radius: 22px;
    overflow: hidden;
    color: var(--gold);
    text-align: center;
  }
  .card--front { top: 125px; background: var(--card-black); }
  .card--back { top: 641px; background: var(--bronze-dark); }

  .flourish {
    position: absolute;
    left: 150px;
    width: 423px;
    height: 54px;
    background: linear-gradient(90deg, transparent, rgba(201,160,99,0.35) 20%, rgba(201,160,99,0.5) 50%, rgba(201,160,99,0.35) 80%, transparent);
    border-radius: 27px;
  }
  .flourish--top { top: 0; }
  .flourish--bottom { bottom: 0; }

  .holder-name {
    position: absolute;
    top: 144px;
    left: 0; right: 0;
    font-size: 37px;
    line-height: 44px;
    font-weight: 600;
    letter-spacing: 1px;
  }
  .holder-title {
    position: absolute;
    top: 190px;
    left: 128px; right: 128px;
    display: flex;
    align-items: center;
    gap: 12px;
    font-size: 16px;
    line-height: 20px;
    letter-spacing: 1px;
  }
  .holder-title::before, .holder-title::after {
    content: "";
    flex: 1;
    height: 2px;
    background: linear-gradient(90deg, transparent, var(--gold-soft));
  }
  .holder-title::after { background: linear-gradient(90deg, var(--gold-soft), transparent); }

  .contact {
    position: absolute;
    top: 234px;
    left: 0; right: 0;
    font-size: 18px;
    line-height: 25px;
    font-weight: 400;
  }
  .social {
    position: absolute;
    top: 316px;
    left: 0; right: 0;
    display: flex;
    justify-content: center;
    gap: 7px;
  }
  .social-link {
    width: 22px; height: 22px;
    background: var(--gold);
    border-radius: 2px;
  }

  .glyph-field {
    position: absolute;
    inset: 0;
    background:
      radial-gradient(ellipse 60% 45% at 50% 50%, rgba(8,6,4,0.92), rgba(8,6,4,0.55) 70%, transparent 100%),
      linear-gradient(180deg, var(--bronze-mid), var(--bronze-light) 35%, var(--bronze-mid) 70%, var(--bronze-dark));
  }
  .brand-name {
    position: absolute;
    top: 172px;
    left: 0; right: 0;
    font-size: 40px;
    line-height: 48px;
    font-weight: 700;
    letter-spacing: 3px;
  }
  .back-web {
    position: absolute;
    top: 362px;
    left: 0; right: 0;
    font-size: 18px;
    line-height: 24px;
    font-weight: 400;
  }
</style>
</head>
<body>
  <section class="card card--front" aria-label="Business card front">
    <div class="flourish flourish--top" role="img" aria-label="Gold scrollwork ornament"></div>
    <h1 class="holder-name">Marisol T. Pike</h1>
    <p class="holder-title">Owner</p>
    <p class="contact">555.210.4473<br>www.Lunaryth.example</p>
    <div class="social" aria-label="Social profiles">
      <span class="social-link" aria-label="Social profile one"></span>
      <span class="social-link" aria-label="Social profile two"></span>
      <span class="social-link" aria-label="Social profile three"></span>
    </div>
    <div class="flourish flourish--bottom" role="img" aria-label="Gold scrollwork ornament"></div>
  </section>

  <section class="card card--back" aria-label="Business card back">
    <div class="glyph-field" role="img" aria-label="Carved hieroglyph wall texture in bronze tones"></div>
    <h2 class="brand-name">LUNARYTH</h2>
    <p class="back-web">www.Lunaryth.example</p>
  </section>
</body>
</html>
```